Brindle-Carriers Invites Companies to the Cloud

My company works with business helping them strategize on moving services to the Cloud. I am running a campaign in which I am reaching out to C-Level Executives in the Greater Los Angeles area and trying to arrange strategy meetings about their IT and Cloud Services. I want a mailer to send in between phone calls and emails.

Main focuses are
- Software Defined Wide Area Networks (we call Smart Internet)
- Cyber Security
- Desk Suite 12 and Hosted Telephony

Here is a link to my website: http://www.brindle-carriers.example
Here is the link to my Netwove Page https://www.netwove.example/public-profile/settings?trk=prof-edit-edit-public_profile

See what you can come up.

Target Market(s)

CEO, Presidents of companies

Industry/Entity Type

Information Technology

Requirements
Must have
• Must be memorable. I have seen way to many pictures of clouds and a weird guy with a hand touching it. I want my card to stand out. Some how and I am not sure how.
Should not have
• The same thing every other IT company has. Show me something make me laugh.

```html
<!DOCTYPE html>
<html lang="en">
<head>
<meta charset="utf-8">
<title>Brindle-Carriers Mailer</title>
<link href="https://fonts.googleapis.com/css2?family=Roboto+Condensed:wght@400;700&family=Open+Sans:wght@400&family=Yanone+Kaffeesatz:wght@400&display=swap" rel="stylesheet">
<style>
  :root {
    --navy: #2c3082;
    --navy-deep: #1f2c6e;
    --ink: #23285f;
    --headline: #2b78ad;
    --periwinkle: #6f86cc;
    --cyan: #63c6ea;
    --rule: #8fb0d8;
    --stage: #e4e6ea;
    --white: #ffffff;
  }
  * { box-sizing: border-box; margin: 0; padding: 0; }
  html, body { width: 1200px; height: 1200px; overflow: hidden; }
  body {
    background: var(--stage);
    font-family: "Roboto Condensed", Arial, sans-serif;
    position: relative;
  }
  .card {
    position: absolute;
    left: 240px;
    width: 720px;
    height: 558px;
    overflow: hidden;
    box-shadow: 0 6px 18px rgba(0,0,0,.25);
  }
  /* ---------- Address side ---------- */
  .card--address { top: 28px; background: var(--white); }
  .address__sky {
    position: absolute; inset: 0;
    background:
      radial-gradient(ellipse 40% 38% at 62% 55%, rgba(255,255,255,.95), rgba(255,255,255,0) 70%),
      linear-gradient(120deg, #ffffff 0%, #ffffff 40%, #c7d1ef 62%, var(--periwinkle) 100%);
  }
  .brand {
    position: absolute; left: 40px; top: 40px;
    display: flex; align-items: center; gap: 12px;
  }
  .brand__dot {
    width: 34px; height: 34px; border-radius: 50%;
    background: #dfe9f7; border: 3px solid var(--navy);
  }
  .brand__name {
    font-family: "Open Sans", Arial, sans-serif;
    font-size: 25px; color: var(--navy); line-height: 1;
  }
  .brand__tag {
    position: absolute; left: 128px; top: 74px;
    font-family: "Open Sans", Arial, sans-serif;
    font-size: 10px; color: var(--navy);
  }
  .intro {
    position: absolute; left: 37px; top: 96px;
    font-family: "Open Sans", Arial, sans-serif;
    font-size: 16px; letter-spacing: 1.5px; color: #4a4f63; white-space: nowrap;
  }
  .headline {
    position: absolute; left: 36px; top: 116px;
    font-size: 30px; font-weight: 400; color: var(--headline);
    letter-spacing: -.3px; line-height: 36px; white-space: nowrap;
  }
  .mission {
    position: absolute; left: 37px; top: 162px; width: 290px;
    font-size: 15px; line-height: 17.9px; color: var(--ink);
    text-align: justify;
  }
  .mission strong { font-weight: 700; }
  .call {
    position: absolute; left: 35px; top: 300px;
    font-size: 27px; line-height: 34px; color: var(--navy); white-space: nowrap;
  }
  .web-pill {
    position: absolute; left: 31px; top: 343px;
    width: 293px; height: 37px; border-radius: 18px;
    background: var(--navy); color: var(--white);
    font-family: "Open Sans", Arial, sans-serif; font-size: 17px;
    display: flex; align-items: center; justify-content: center;
    box-shadow: 0 6px 6px rgba(0,0,0,.25);
  }
  .web-pill::after {
    content: ""; position: absolute; left: 138px; bottom: -8px;
    border: 8px solid transparent; border-top-color: var(--navy); border-bottom: 0;
  }
  .devices-photo {
    position: absolute; left: 0; top: 397px; width: 348px; height: 122px;
    background: linear-gradient(180deg, rgba(111,134,204,0) 0%, #8fa3dc 40%, #7d93d4 100%);
  }
  .divider {
    position: absolute; left: 348px; top: 179px; width: 1px; height: 340px;
    background: var(--rule);
  }
  .address-line {
    position: absolute; left: 373px; width: 314px; height: 1px;
    background: var(--rule);
  }
  .footer-band {
    position: absolute; left: 0; bottom: 0; width: 100%; height: 39px;
    background: var(--navy);
  }
  /* ---------- Message side ---------- */
  .card--message {
    top: 614px;
    background: linear-gradient(180deg, var(--cyan) 0%, #3d8fcc 40%, #2b5fa8 65%, var(--navy-deep) 100%);
  }
  .message__glow {
    position: absolute; left: 140px; top: 40px; width: 440px; height: 320px;
    border-radius: 50%;
    background: radial-gradient(ellipse at center, rgba(255,255,255,.35), rgba(255,255,255,0) 70%);
  }
  .brand--center {
    position: absolute; left: 0; right: 0; top: 144px;
    display: flex; justify-content: center; align-items: center; gap: 14px;
  }
  .brand--center .brand__dot { width: 42px; height: 42px; }
  .brand--center .brand__name { font-size: 37px; color: var(--ink); }
  .brand__tag--center {
    position: absolute; left: 0; right: 0; top: 191px; text-align: center;
    font-family: "Open Sans", Arial, sans-serif; font-size: 14px; color: var(--ink);
  }
  .security-art {
    position: absolute; left: 57px; top: 212px; width: 620px; height: 170px;
    border-radius: 12px;
    background: linear-gradient(180deg, rgba(190,230,250,.55) 0%, rgba(120,190,235,.45) 55%, rgba(60,120,190,0) 100%);
  }
  .message__title {
    position: absolute; left: 0; right: 0; top: 386px; text-align: center;
    font-family: "Yanone Kaffeesatz", "Roboto Condensed", sans-serif;
    font-size: 34px; line-height: 40px; color: var(--white); letter-spacing: .5px; font-weight: 400;
  }
  .message__body {
    position: absolute; left: 20px; right: 20px; top: 430px; text-align: center;
    font-family: "Open Sans", Arial, sans-serif; font-size: 16.5px; line-height: 20px;
    color: var(--white);
  }
  .message__rule {
    position: absolute; left: 0; right: 0; height: 1px;
    background: linear-gradient(90deg, rgba(120,200,240,.9) 0%, rgba(120,200,240,.5) 30%, rgba(120,200,240,0) 32%, rgba(120,200,240,0) 73%, rgba(120,200,240,.5) 75%, rgba(120,200,240,.9) 100%);
  }
  .message__web {
    position: absolute; left: 0; right: 0; top: 500px; text-align: center;
    font-family: "Open Sans", Arial, sans-serif; font-size: 17px; line-height: 22px;
    letter-spacing: 4px; color: #9aa9cf;
  }
</style>
</head>
<body>

<section class="card card--address">
  <div class="address__sky" role="img" aria-label="Photo of a bright sky with soft white clouds"></div>

  <div class="brand">
    <span class="brand__dot"></span>
    <span class="brand__name">Brindle-Carriers</span>
  </div>
  <p class="brand__tag">So much more than just telco</p>

  <p class="intro">Brindle-Carriers is carrier agency that specializes in</p>
  <h1 class="headline">CLOUD, CARRIERS AND CONTINUITY.</h1>

  <p class="mission"><strong>Our mission</strong> is to provide our customers with options that not only allow them to reach their efficiency goals but also reduce costs. We offer free auditing and consulting in which we can review your current expenses and discuss with your team leaders what they hope to achieve with a new solution.</p>

  <p class="call">Call us today 310-555-0148</p>
  <div class="web-pill">www.brindle-carriers.example</div>

  <div class="devices-photo" role="img" aria-label="Photo of raised hands holding tablets, laptops and phones showing clouds"></div>

  <div class="divider"></div>
  <div class="address-line" style="top:278px"></div>
  <div class="address-line" style="top:318px"></div>
  <div class="address-line" style="top:359px"></div>
  <div class="address-line" style="top:403px"></div>

  <div class="footer-band"></div>
</section>

<section class="card card--message">
  <div class="message__glow"></div>

  <div class="brand--center">
    <span class="brand__dot"></span>
    <span class="brand__name">Brindle-Carriers</span>
  </div>
  <p class="brand__tag--center">So much more than just telco</p>

  <div class="security-art" role="img" aria-label="Illustration of glowing cloud security panels with shields, keys, locks and firewall symbols over a world map"></div>

  <h2 class="message__title">It’s Time to Take a Fresh Look at Your Technology</h2>
  <p class="message__body">Make the Cloud work for you. It’s never been easier to leverage enterprise class<br>software and infrastructure. Let our consultants show you how to take<br>advantage and create a Cloud solution that is right for your business.</p>

  <div class="message__rule" style="top:507px"></div>
  <div class="message__rule" style="top:515px"></div>
  <p class="message__web">www.brindle-carriers.example</p>
</section>

</body>
</html>
```